Renata Quisby

Luxury And Style -

Black - White & Gold

Target Market(s)

Fashion

Industry/Entity Type

Fashion

Requirements
Must have
• High-End
Nice to have
• We will Print on Silk Paper

```html
<!DOCTYPE html>
<html lang="en">
<head>
<meta charset="utf-8">
<title>Renata Quisby — Letterhead</title>
<link rel="stylesheet" href="https://fonts.googleapis.com/css2?family=Jost:wght@300;400;600&display=swap">
<style>
  :root {
    --backdrop: #2a2c30;
    --paper: #f1eee8;
    --paper-shade: #e6e3dd;
    --ink: #141414;
    --ink-soft: #2b2b2b;
  }
  * { margin: 0; padding: 0; box-sizing: border-box; }
  html, body {
    width: 1200px; height: 1199px; overflow: hidden;
    background: var(--backdrop);
  }
  .letterhead {
    position: absolute; left: 200px; top: 30px;
    width: 800px; height: 1140px;
    background: var(--paper);
    font-family: "Jost", sans-serif;
    color: var(--ink);
    overflow: hidden;
  }
  .backdrop-shape { position: absolute; left: 0; top: 0; }
  .brand {
    position: absolute; left: 0; top: 176px; width: 100%;
    text-align: center;
  }
  .brand-name {
    font-size: 28px; font-weight: 400; letter-spacing: 2.5px;
    text-transform: uppercase; line-height: 1;
  }
  .brand-tagline {
    margin-top: 10px;
    font-size: 13px; font-weight: 300; letter-spacing: 0.6px;
    text-transform: uppercase;
  }
  .header-rule {
    position: absolute; left: 136px; top: 278px;
    width: 530px; height: 0; border-top: 1.5px solid var(--ink-soft);
  }
  .letter-body {
    position: absolute; left: 98px; top: 370px; width: 590px;
    font-size: 10.4px; font-weight: 600; line-height: 12.5px;
  }
  .letter-body p { margin-bottom: 12px; }
  .letter-body p.tight { margin-bottom: 0; }
  .contact {
    position: absolute; top: 1011px;
    font-size: 17px; font-weight: 400; line-height: 24.5px;
    color: var(--ink-soft); list-style: none;
  }
  .contact-left { left: 56px; }
  .contact-right { left: 532px; }
  .contact li { display: flex; align-items: center; }
  .contact-right li { padding-left: 20px; }
  .contact .icon { width: 12px; height: 12px; margin-right: 12px; flex: none; }
  .contact-right .pin { position: absolute; left: 0; top: 6px; width: 11px; height: 14px; }
</style>
</head>
<body>
<main class="letterhead">
  <svg class="backdrop-shape" width="800" height="1140" aria-hidden="true">
    <polygon points="240,690 620,690 430,1140" fill="var(--paper-shade)"/>
  </svg>

  <header class="brand">
    <div class="brand-name">Renata Quisby</div>
    <div class="brand-tagline">Luxury and Style</div>
  </header>
  <div class="header-rule"></div>

  <section class="letter-body">
    <p>Lorem ipsum dolor sit amet, consectetur adipiscing elit, sed do eiusmod tempor incididunt ut labore et dolore magna aliqua. Quis ipsum suspendisse ultrices gravida. Risus commodo viverra maecenas accumsan lacus vel facilisis.</p>
    <p>Lorem ipsum dolor sit amet, consectetur adipiscing elit, sed do eiusmod tempor incididunt ut labore et dolore magna aliqua. Quis ipsum suspendisse ultrices gravida. Risus commodo viverra maecenas accumsan lacus vel facilisis.</p>
    <p>Lorem ipsum dolor sit amet, consectetur adipiscing elit, sed do eiusmod tempor incididunt ut labore et dolore magna aliqua. Quis ipsum suspendisse ultrices gravida. Risus commodo viverra maecenas accumsan lacus vel facilisis.</p>
    <p>Lorem ipsum dolor sit amet, consectetur adipiscing elit, sed do eiusmod tempor incididunt ut labore et dolore magna aliqua. Quis ipsum suspendisse ultrices gravida. Risus commodo viverra maecenas accumsan lacus vel facilisis.</p>
    <p class="tight">Lorem ipsum dolor sit amet, consectetur adipiscing elit, sed do eiusmod tempor incididunt ut labore et dolore magna aliqua. Quis ipsum suspendisse ultrices gravida. Risus commodo viverra maecenas accumsan lacus vel facilisis.</p>
    <p class="tight">Lorem ipsum dolor sit amet, consectetur adipiscing elit, sed do eiusmod tempor incididunt ut labore et dolore magna aliqua. Quis ipsum suspendisse ultrices gravida. Risus commodo viverra maecenas accumsan lacus vel facilisis.</p>
    <p class="tight">Lorem ipsum dolor sit amet, consectetur adipiscing elit, sed do eiusmod tempor incididunt ut labore et dolore magna aliqua. Quis ipsum suspendisse ultrices gravida. Risus commodo viverra maecenas accumsan lacus vel facilisis.</p>
    <p>Lorem ipsum dolor sit amet, consectetur adipiscing elit, sed do eiusmod tempor incididunt ut labore et dolore magna aliqua. Quis ipsum suspendisse ultrices gravida. Risus commodo viverra maecenas accumsan lacus vel facilisis.</p>
    <p class="tight">Lorem ipsum dolor sit amet, consectetur adipiscing elit, sed do eiusmod tempor incididunt ut labore et dolore magna aliqua. Quis ipsum suspendisse ultrices gravida. Risus commodo viverra maecenas accumsan lacus vel facilisis.</p>
    <p>Lorem ipsum dolor sit amet, consectetur adipiscing elit, sed do eiusmod tempor incididunt ut labore et dolore magna aliqua. Quis ipsum suspendisse ultrices gravida. Risus commodo viverra maecenas accumsan lacus vel facilisis.</p>
    <p>Lorem ipsum dolor sit amet, consectetur adipiscing elit, sed do eiusmod tempor incididunt ut labore et dolore magna aliqua. Quis ipsum suspendisse ultrices gravida. Risus commodo viverra maecenas accumsan lacus vel facilisis.</p>
    <p>Lorem ipsum dolor sit amet, consectetur adipiscing elit, sed do eiusmod tempor incididunt ut labore et dolore magna aliqua. Quis ipsum suspendisse ultrices gravida. Risus commodo viverra maecenas accumsan lacus vel facilisis.</p>
    <p class="tight">Lorem ipsum dolor sit amet, consectetur adipiscing elit, sed do eiusmod tempor incididunt ut labore et dolore magna aliqua. Quis ipsum suspendisse ultrices gravida. Risus commodo viverra maecenas accumsan lacus vel facilisis.</p>
    <p class="tight">Lorem ipsum dolor sit amet, consectetur adipiscing elit, sed do eiusmod tempor incididunt ut labore et dolore magna aliqua. Quis ipsum suspendisse ultrices gravida. Risus commodo viverra maecenas accumsan lacus vel facilisis.</p>
    <p class="tight">Lorem ipsum dolor sit amet, consectetur adipiscing elit, sed do eiusmod tempor incididunt ut labore et dolore magna aliqua. Quis ipsum suspendisse ultrices gravida. Risus commodo viverra maecenas accumsan lacus vel facilisis.</p>
  </section>

  <ul class="contact contact-left">
    <li>
      <svg class="icon" viewBox="0 0 12 12" aria-hidden="true"><path d="M2.2 0.8 L4.2 0.8 L5 3.4 L3.7 4.5 Q4.9 7 7.5 8.3 L8.6 7 L11.2 7.8 L11.2 9.8 Q11.2 11.2 9.8 11.2 Q0.8 10.6 0.8 2.2 Q0.8 0.8 2.2 0.8 Z" fill="var(--ink)"/></svg>
      +81 0005551234
    </li>
    <li>
      <svg class="icon" viewBox="0 0 12 12" aria-hidden="true"><circle cx="6" cy="6" r="4.8" fill="none" stroke="var(--ink)" stroke-width="1.4"/></svg>
      +81 0005551234
    </li>
    <li>
      <svg class="icon" viewBox="0 0 12 12" aria-hidden="true"><rect x="0.5" y="2" width="11" height="8" fill="var(--ink)"/><path d="M0.8 2.4 L6 6.6 L11.2 2.4" fill="none" stroke="var(--paper)" stroke-width="1"/></svg>
      renata@rq.studio
    </li>
    <li>
      <svg class="icon" viewBox="0 0 12 12" aria-hidden="true"><circle cx="6" cy="6" r="5.2" fill="var(--ink)"/><path d="M1 6 H11 M6 0.8 Q3 6 6 11.2 M6 0.8 Q9 6 6 11.2" fill="none" stroke="var(--paper)" stroke-width="0.8"/></svg>
      www.rq.studio
    </li>
  </ul>

  <ul class="contact contact-right">
    <svg class="pin" viewBox="0 0 11 14" aria-hidden="true"><path d="M5.5 0.5 Q10.5 0.5 10.5 5.2 Q10.5 8.6 5.5 13.5 Q0.5 8.6 0.5 5.2 Q0.5 0.5 5.5 0.5 Z" fill="var(--ink)"/><circle cx="5.5" cy="5.2" r="1.8" fill="var(--paper)"/></svg>
    <li>S4-12 &amp; S7-18</li>
    <li>Block 020 - 145, K9 Street</li>
    <li>Da Nang City, Vietnam</li>
  </ul>
</main>
</body>
</html>
```